MOREVI VEGAN SUSHI

www.morevi-restaurant.de
We are open in 2018 and are an innovative restaurant from Munich. We would like a cool design for our drinks and food menu. It's very simple at the moment. See the File menu. In any case, our logo should appear. On the website we use neutraface as a font. But it's not a must. We are only open in the evening and appeal to a young, upscale audience.

```html
<!DOCTYPE html>
<html lang="de">
<head>
<meta charset="utf-8">
<title>MOREVI Vegan Sushi – Menu</title>
<link rel="stylesheet" href="https://fonts.googleapis.com/css2?family=Montserrat:wght@400;500;600;700;800;900&family=Playfair+Display:wght@700;900&display=swap">
<style>
  :root{
    --ink:#0d0d0d;
    --paper:#ffffff;
    --paper-soft:#ececec;
    --red:#d7141a;
    --grey-band:#4a4a4a;
    --text-dark:#1a1a1a;
    --stage:#efefef;
  }
  *{box-sizing:border-box;margin:0;padding:0}
  html,body{width:900px;height:1200px;overflow:hidden}
  body{background:var(--stage);font-family:"Montserrat",sans-serif;position:relative}
  .page{position:absolute;top:296px;width:430px;height:608px;overflow:hidden;box-shadow:0 4px 14px rgba(0,0,0,.18)}
  .cover{left:10px;background:var(--ink);color:var(--paper)}
  .inside{left:460px;background:linear-gradient(180deg,#f7f7f7,var(--paper-soft));color:var(--text-dark)}

  /* cover */
  .cover-frame{position:absolute;inset:14px;border:1px solid rgba(255,255,255,.55)}
  .brand{position:absolute;top:32px;left:0;width:100%;text-align:center}
  .brand-dot{width:30px;height:30px;border-radius:50%;background:var(--paper);margin:0 auto 6px}
  .brand-name{font-size:9px;font-weight:500;letter-spacing:4px}
  .welcome{position:absolute;top:102px;width:100%;text-align:center;font-family:"Playfair Display",serif;font-weight:900;font-size:30px}
  .welcome-rule{position:absolute;top:146px;left:132px;width:166px;height:2px;background:var(--red)}
  .menu-word{position:absolute;left:0;width:100%;text-align:center;font-weight:900;font-size:58px;line-height:1;letter-spacing:4px}
  .menu-word.top{top:160px;color:var(--paper)}
  .menu-word.bottom{top:216px;color:var(--red)}
  .sushi-bit{position:absolute;border-radius:50%;background:radial-gradient(circle,#f4e3c7 35%,#e0774a 36%,#f7f4ee 55%,#2b2b2b 70%)}
  .chef-band{position:absolute;top:288px;left:66px;width:300px;height:28px;background:linear-gradient(90deg,#2a2a2a,var(--grey-band) 50%,#2a2a2a);text-align:center;line-height:28px;font-weight:700;font-size:13px;letter-spacing:1.5px}
  .cover-photo{position:absolute;top:330px;left:30px;width:370px;height:160px;background:linear-gradient(180deg,#0d0d0d 0%,#6b3b22 35%,#d88a5a 55%,#e9e9e9 75%,#1a1a1a 100%);border-radius:4px}
  .site{position:absolute;bottom:28px;width:100%;text-align:center;font-size:9px;letter-spacing:4px}
  .cover .site{color:var(--paper)}

  /* inside */
  .inside-photo{position:absolute;top:0;left:0;width:100%;height:230px;background:linear-gradient(160deg,#4a2e1e 0%,#c87a4a 35%,#e8d2b2 60%,#f3f3f3 100%)}
  .headline-box{position:absolute;top:214px;left:14px;padding:0 10px;height:32px;background:var(--red);color:var(--paper);font-weight:800;font-size:21px;line-height:32px;letter-spacing:1px}
  .headline-dark{position:absolute;top:192px;left:190px;font-weight:800;font-size:24px;color:var(--text-dark)}
  .tag{position:absolute;height:22px;padding:0 12px;font-weight:700;font-size:12px;line-height:22px;color:var(--paper)}
  .tag.red{background:var(--red)}
  .tag.black{background:var(--ink)}
  .price{position:absolute;height:26px;padding:0 9px;font-weight:600;font-size:12px;line-height:26px;color:var(--paper)}
  .price.black{background:var(--ink)}
  .price.red{background:var(--red)}
  .dish-list{position:absolute;list-style:none;font-size:9px;font-weight:600;line-height:15px;text-transform:none}
  .offer{position:absolute;left:14px;font-size:7.5px;line-height:11px;font-weight:500}
  .offer .amount{position:absolute;left:100px;top:10px;color:var(--red);font-size:10px;font-weight:600}
  .offer .accent{color:var(--red);font-weight:700}
  .thumb{position:absolute;border-radius:50%;background:radial-gradient(circle,#e98a5c 30%,#f5f2ea 55%,#cfcfcf 80%)}
  .thumb-sq{position:absolute;width:18px;height:18px;border-radius:4px;background:radial-gradient(circle,#e06b3f 30%,#f5f2ea 60%,#999 90%)}
  .rules{position:absolute;inset:0}
  .inside .site{color:var(--text-dark)}
</style>
</head>
<body>

<section class="page cover">
  <div class="cover-frame"></div>
  <div class="brand">
    <div class="brand-dot"></div>
    <div class="brand-name">MOREVI</div>
  </div>
  <h1 class="welcome">Welcome</h1>
  <div class="welcome-rule"></div>
  <div class="menu-word top">ME</div>
  <div class="menu-word bottom">NU</div>
  <div class="sushi-bit" role="img" aria-label="Sushi roll piece" style="top:176px;left:128px;width:22px;height:22px"></div>
  <div class="sushi-bit" role="img" aria-label="Sushi roll piece" style="top:232px;left:282px;width:22px;height:22px"></div>
  <div class="chef-band">CHEF MENÜ mit Aperitiva</div>
  <div class="cover-photo" role="img" aria-label="Sushi rolls on a white plate with reflection"></div>
  <div class="site">www.morevi-restaurant.de</div>
</section>

<section class="page inside">
  <div class="inside-photo" role="img" aria-label="Close-up of vegan sushi rolls with chopsticks"></div>
  <div class="headline-dark">VEGAN</div>
  <div class="headline-box">DELIGHTFUL</div>

  <svg class="rules" width="430" height="608" aria-hidden="true">
    <g fill="none" stroke="#d7141a" stroke-width="1">
      <polyline points="200,240 200,236 400,236 400,300"/>
      <polyline points="200,412 200,408 400,408 400,470"/>
      <polyline points="14,318 120,318"/>
      <polyline points="14,400 120,400"/>
      <polyline points="12,452 12,565 200,565 200,480"/>
    </g>
  </svg>

  <div class="tag red" style="top:226px;left:300px">SET 1</div>
  <div class="price black" style="top:252px;left:352px">33,90</div>
  <ul class="dish-list" style="top:262px;left:212px">
    <li>HOSOMAKI</li><li>FUTOMAKI</li><li>NIGIRI</li><li>KÜRBISKROKETTEN</li>
    <li>WAKAME GURKEN SALAT</li><li>PICKLES</li><li>GYOZA TEIGTASCHEN</li><li>SUSHI CAKE</li>
  </ul>

  <div class="offer" style="top:324px">
    CHEF MENÜ mit Aperitiva<br>(für 2 Personen)<br>Kleine Portion RAMENSUPPE<br>mit Gemüse &amp; Nudeln<br>MINI SET <span class="accent">DESSERT</span>
    <span class="amount">81,00€</span>
  </div>
  <div class="thumb" role="img" aria-label="Sushi roll" style="top:324px;left:158px;width:34px;height:34px"></div>

  <div class="offer" style="top:406px">
    OMAKASE<br>(für 2 Personen)<br><span class="accent">EDAMAME</span><br>OMAKASE SET mit 6 Sorten<br><span class="accent">PANA COTTA</span> mit Beeren
    <span class="amount">68,00€</span>
  </div>
  <div class="thumb" role="img" aria-label="Nigiri piece" style="top:404px;left:158px;width:34px;height:34px"></div>

  <div class="tag red" style="top:398px;left:300px">SET 2</div>
  <div class="price black" style="top:424px;left:352px">31,90€</div>
  <ul class="dish-list" style="top:434px;left:212px">
    <li>HOSOMAKI</li><li>FUTOMAKI</li><li>PICKLES</li><li>SUSHI "THUNA" CAKE</li>
    <li>Crispy AUBERGINEN mit Mayo</li><li>AUBERGINE DENGAKU</li>
  </ul>

  <div class="tag black" style="top:444px;left:130px">SET 3</div>
  <div class="price red" style="top:474px;left:132px">28,90€</div>
  <ul class="dish-list" style="top:474px;left:20px">
    <li>HOSOMAKI</li><li>FUTOMAKI</li><li>NIGIRI</li><li>GEMÜSE TEMPURA</li>
    <li>Crispy TOFUSTICKS mit Mayo</li><li>WAKAME SHIRA AE</li>
  </ul>
  <div class="thumb-sq" role="img" aria-label="Maki piece" style="top:430px;left:172px"></div>
  <div class="thumb-sq" role="img" aria-label="Maki piece" style="top:506px;left:178px"></div>
  <div class="thumb-sq" role="img" aria-label="Maki piece" style="top:528px;left:178px"></div>

  <div class="site">www.morevi-restaurant.de</div>
</section>

</body>
</html>
```